New design for PeopleDeskly

We are at the start of the process of evolving an existing business, and have just developed a new logo that will guide the look and feel of the rest of the site.

PeopleDeskly.com.au will be the place to go for small business owners that need guidance and tools on how to look after HR functions such as recruitment and performance management amongst other aspects.

The existing site that is going to be evolved in www.staffingpathguide.com.au - while some of the content will remain, the entire look of the site needs to change, and a new homepage and other pages need to be developed.

For this project, we'd like the new homepage to be designed to lead the way for how the rest of the pages will look moving forward.

We're looking for a clean, clear and modern design. It should not feel cluttered or busy

The wireframe for the new homepage, and another landing page are attached.

Target Market(s)

Small and medium business owners - slightly male skew

Industry/Entity Type

Small Business

Requirements
Must have
• - Should be clean and simple
- The overall feel from the new logo (attached to the project) should be integrated into all elements of the site
- Should communicate that the site is easy to navigate
- Should communicate that the site is friendly and approachable
- Should communicate that the site is professional (for small businesses)
Nice to have
• This homepage for this site is quite a good design reference in terms of clean design.

http://www.chorebadger.example/

For PeopleDeskly though, the 3 boxes under the main image should appear above the fold though.

Also, happy for one other colour to be introduced to highlight call to action buttons etc.
Should not have
• Must not be cluttered
Should not introduce more than one additional colour to the existing colours from the logo

```html
<!DOCTYPE html>
<html lang="en">
<head>
<meta charset="utf-8">
<title>PeopleDeskly – Home</title>
<link href="https://fonts.googleapis.com/css2?family=PT+Sans:wght@400;700&family=Arimo:wght@400;700&display=swap" rel="stylesheet">
<style>
:root{
  --blue:#0d6fb8;
  --blue-dark:#0a4f8c;
  --blue-light:#2a8ad4;
  --nav-top:#2e8fd6;
  --nav-bottom:#0b5a9e;
  --side-bg:#0c5fa3;
  --active-top:#6e6e6e;
  --active-bottom:#3d3d3d;
  --ink:#333;
  --heading:#4a4a4a;
  --green:#5a9a1e;
  --green-dark:#3f7512;
  --footer:#3a3a3c;
  --footer-ink:#fff;
  --muted:#888;
}
*{box-sizing:border-box;margin:0;padding:0}
html,body{width:1141px;height:1200px;overflow:hidden;background:#fff;font-family:"Arimo",Arial,sans-serif;color:var(--ink)}
.page{position:relative;width:1141px;height:1200px}
.header{position:absolute;left:0;top:0;width:1141px;height:119px;background:linear-gradient(#f4f4f4,#e9e9e9);border-top:4px solid var(--blue)}
.brand{position:absolute;left:13px;top:0;width:256px;height:93px;background:#fff;box-shadow:0 1px 4px rgba(0,0,0,.25);display:flex;align-items:center;justify-content:center;gap:10px}
.brand-dot{width:30px;height:30px;border-radius:50%;background:var(--blue)}
.brand-name{font-family:"PT Sans",sans-serif;font-weight:700;font-size:30px;color:var(--blue)}
.contact{position:absolute;right:12px;top:52px;display:flex;align-items:center;gap:10px;font-size:13px;line-height:17px;color:#333}
.nav{position:absolute;left:0;top:119px;width:1141px;height:46px;background:linear-gradient(var(--nav-top),var(--nav-bottom));display:flex;padding-left:13px}
.nav a{display:flex;align-items:center;justify-content:center;color:#fff;text-decoration:none;font-size:16px;border-right:1px solid rgba(0,0,0,.25);box-shadow:inset -1px 0 rgba(255,255,255,.2)}
.nav a.active{background:linear-gradient(#5aa8e4,#2a86cc)}
.side{position:absolute;left:13px;top:176px;width:256px;list-style:none;background:var(--side-bg)}
.side li{height:41px;display:flex;align-items:center;padding-left:18px;color:#fff;font-size:16px;border-bottom:1px solid #0a4c85;border-top:1px solid #1a73bb}
.side li::before{content:"";width:7px;height:7px;border:2px solid #fff;border-radius:50%;margin-right:16px}
.side li.active{background:linear-gradient(var(--active-top),var(--active-bottom))}
.hero{position:absolute;left:280px;top:176px;width:850px;height:331px;background:linear-gradient(100deg,#cfe3f4 0%,#a9cbe8 35%,#e6eef5 60%,#8b8f98 100%);box-shadow:0 2px 6px rgba(0,0,0,.3)}
.features{position:absolute;left:0;top:562px;width:1141px;height:380px}
.feature{position:absolute;top:0;width:360px;text-align:center}
.feature-icon{display:block;margin:0 auto}
.feature h2{font-family:"PT Sans",sans-serif;font-weight:400;font-size:27px;color:var(--heading);margin-top:26px}
.feature p{font-size:13px;line-height:17.5px;margin-top:8px}
.about{left:-17px}.about p{padding:0 60px}
.news{left:399px}.news .item{text-align:left;padding:0 60px;font-size:13px;line-height:17.5px;margin-top:8px}
.news .item+.item{margin-top:20px}
.news a{color:#333}
.partners{left:765px}
.divider{position:absolute;top:70px;width:1px;height:230px;background:linear-gradient(transparent,#ccc,transparent)}
.badges{display:grid;grid-template-columns:112px 112px;gap:22px 30px;justify-content:center;margin-top:22px}
.badge{height:34px;border-radius:4px;background:#d9d9d9}
.badge.dark{background:#555}
.badge.gold{background:#c9a448}
.badge.blue{background:#7fa6c8}
.badge.red{background:#e0603a}
.btn-more{height:32px;border-radius:16px;background:linear-gradient(#7ab83a,var(--green-dark));color:#fff;font-size:11px;font-weight:700;display:flex;align-items:center;justify-content:center;align-self:center}
.footer{position:absolute;left:0;top:981px;width:1141px;height:219px;background:var(--footer);color:var(--footer-ink)}
.footer h3{font-size:16px;font-weight:700;margin-bottom:14px}
.col{position:absolute;top:20px}
.col ul{list-style:none;font-size:13px;line-height:20.5px}
.col p{font-size:13px;line-height:20px}
.signup{display:flex;gap:10px;margin-top:18px}
.signup span{width:270px;height:34px;background:#4b4b4d;border:1px solid #2d2d2d}
.signup b{width:100px;height:34px;border-radius:17px;background:linear-gradient(#7ab83a,var(--green-dark));display:flex;align-items:center;justify-content:center;font-size:14px}
.socials{display:flex;gap:8px}
.socials i{width:24px;height:24px;border-radius:4px;background:#8fb6d9}
.foot-brand{margin-top:30px;display:flex;align-items:center;gap:8px;color:#666;font-family:"PT Sans",sans-serif;font-weight:700;font-size:28px}
.foot-brand em{width:28px;height:28px;border-radius:50%;background:#666}
</style>
</head>
<body>
<div class="page">
  <header class="header">
    <div class="brand"><span class="brand-dot"></span><span class="brand-name">PeopleDeskly</span></div>
    <div class="contact">
      <svg width="34" height="26" viewBox="0 0 34 26"><rect x="3" y="9" width="28" height="15" rx="3" fill="#777"/><path d="M2 9 Q17 -2 32 9 L28 12 Q17 4 6 12Z" fill="#555"/><circle cx="17" cy="16" r="4" fill="#ddd"/></svg>
      <div>+(00)12 34 55501460<br>+(00)12 34 55501459</div>
    </div>
  </header>

  <nav class="nav">
    <a class="active" style="width:95px">Attract</a>
    <a style="width:109px">Recruit</a>
    <a style="width:106px">Induction</a>
    <a style="width:104px">Engage</a>
    <a style="width:152px">Performance</a>
    <a style="width:236px">Termination &amp; Community</a>
    <a style="width:155px">Management</a>
    <a style="width:160px;border-right:0">Redundancy</a>
  </nav>

  <ul class="side">
    <li class="active">Attract</li><li>Recruit</li><li>Induction</li><li>Engage</li>
    <li>Performance</li><li>Termination &amp;Community</li><li>Management</li><li>Redundancy aa</li>
  </ul>

  <div class="hero" role="img" aria-label="Photo of a smiling business team beside a glass globe"></div>

  <section class="features">
    <div class="feature about">
      <svg class="feature-icon" width="124" height="124" viewBox="0 0 124 124"><path d="M14 62 A48 48 0 0 1 62 14" fill="none" stroke="#bbb" stroke-width="2"/><circle cx="62" cy="62" r="46" fill="#2f9be0"/><circle cx="62" cy="62" r="42" fill="#3d3f43"/><circle cx="62" cy="62" r="18" fill="#888"/><circle cx="62" cy="54" r="3" fill="#3d3f43"/><rect x="59" y="60" width="6" height="14" fill="#3d3f43"/></svg>
      <h2>About</h2>
      <p>Lorem Ipsum is simply dummy text of the printing and typesetting industry. Lorem Ipsum has been the industry's standard dummy text ever since the 1500s, when an unknown printer took a galley of type and scrambled it to make a type specimen book. It has survived not only five centuries, but also the leap into electronic typesetting, remaining essentially unchanged.</p>
    </div>
    <div class="divider" style="left:402px"></div>
    <div class="feature news">
      <svg class="feature-icon" width="124" height="124" viewBox="0 0 124 124"><path d="M14 62 A48 48 0 0 1 62 14" fill="none" stroke="#bbb" stroke-width="2"/><circle cx="62" cy="62" r="46" fill="#2f9be0"/><circle cx="62" cy="62" r="42" fill="#3d3f43"/><rect x="44" y="48" width="36" height="28" fill="#ddd"/><rect x="48" y="52" width="28" height="5" fill="#777"/><rect x="48" y="60" width="12" height="12" fill="#999"/><rect x="63" y="61" width="13" height="2" fill="#888"/><rect x="63" y="66" width="13" height="2" fill="#888"/><rect x="63" y="71" width="13" height="2" fill="#888"/></svg>
      <h2>News/community</h2>
      <div class="item">Lorem Ipsum is simply dummy text of the printing and typesetting industry.<br><a>Read More</a></div>
      <div class="item">Lorem Ipsum is simply dummy text of the printing and typesetting industry.<br><a>Read More</a></div>
    </div>
    <div class="divider" style="left:765px"></div>
    <div class="feature partners">
      <svg class="feature-icon" width="124" height="124" viewBox="0 0 124 124"><path d="M14 62 A48 48 0 0 1 62 14" fill="none" stroke="#bbb" stroke-width="2"/><circle cx="62" cy="62" r="46" fill="#2f9be0"/><circle cx="62" cy="62" r="42" fill="#3d3f43"/><circle cx="54" cy="62" r="11" fill="none" stroke="#ddd" stroke-width="4"/><circle cx="70" cy="62" r="11" fill="none" stroke="#ddd" stroke-width="4"/></svg>
      <h2>Social links/Partners</h2>
      <div class="badges">
        <div class="badge dark"></div><div class="badge blue"></div>
        <div class="badge gold"></div><div class="badge" style="background:#e8a04a"></div>
        <div class="badge red"></div><div class="btn-more">VEIW MORE</div>
      </div>
    </div>
  </section>

  <footer class="footer">
    <div class="col" style="left:36px"><h3>Quick links</h3><ul><li>Home</li><li>About</li><li>Work</li><li>Blog</li><li>Contact</li><li>Client Login</li></ul></div>
    <div class="col" style="left:231px"><h3>Powered By</h3><ul><li>PressLeaf</li><li>(hv) Hostvale</li><li>Tally Stats</li><li>OrbitDesk</li><li>PostFinch</li><li>LedgerLoop</li></ul></div>
    <div class="col" style="left:435px;width:400px"><h3>Receive Email Updates</h3><p>Lorem Ipsum is simply dummy text of the printing and typesetting industry. Lorem Ipsum has been the industry's standard dummy text when an unknown printer.</p><div class="signup"><span></span><b>SIGN UP</b></div></div>
    <div class="col" style="left:903px"><h3>Social Network</h3><div class="socials"><i></i><i></i><i></i><i></i></div><div class="foot-brand"><em></em>PeopleDeskly</div></div>
  </footer>
</div>
</body>
</html>
```